Savings/Retirement Infographic

I need an infographic to convey the importance of retirement planning and saving regularly. It must be an attractive and compelling design that people want to read.

The design will primarily be used as a poster, but also as an emailer and a shorter version for an A5 flyer.

Content:

There are only two types of retirement funds
Big or Small

Big retirement funds = Foreign Travel,
Sailing,
Concerts,
Sky Diving,
Fishing,
Golf,
Fine Dining,
Spoiling Grandchildren,
Sandy Beaches.

Small retirement funds = Counting every penny,
Sitting at home,
Relying on family, friends and charity,
Turning off the heating in Winter

Big pensions are acquired over the length of a career with careful planning and motivation.

Small pensions take no effort at all.

Which are you aiming for?

Did you know?
1 in 5 people retiring in 2013 will be below the poverty line?
In the UK, 14% will rely solely on a state pension. That's less than AED 640 per week.
(Source: Harrowgate Cohort of 2013)

Of 100 people aged 25 today, by age 65
1 will be wealthy
4 will be financially independent
5 will still be working
12 will be bankrupt
29 will already be dead
49 will be dependent on others

Of those still living, 86% will rely on friends, relatives and charity.

To retire on $30,000 per annum, you'll need approx.. $600,000 in today's terms.
That's $1,456,380 in 30 years with 3% inflation.
By saving in a bank earning ZERO interest, you need to save $4,045 each month for 30 years
If you invest in the markets and earn 5% interest each year, you only need to save $2,307 each month.
If you manage to get 10% per annum interest, you'll only need to save $934 per month. That's less than AED 3,450.

Please add a bar across the bottom with my contact details, leaving space for my photo and logo. Contact details:

E: rmoss@tidalnest.com
M: 050 8126 473

```html
<!DOCTYPE html>
<html lang="en">
<head>
<meta charset="utf-8">
<title>There Are Only Two Types of Retirement Funds</title>
<link rel="stylesheet" href="https://fonts.googleapis.com/css2?family=Righteous&family=Passion+One:wght@400;700&family=Open+Sans:wght@400;600;700&display=swap">
<style>
  :root {
    --navy: #27338f;
    --blue: #1f7fd0;
    --sky: #bfe3fb;
    --sky-deep: #5fb3ec;
    --orange: #f9b51e;
    --orange-text: #f6a623;
    --paper: #f1f1f3;
    --ink: #1c1c1c;
    --white: #ffffff;
  }
  * { box-sizing: border-box; margin: 0; padding: 0; }
  html, body { width: 1200px; height: 852px; overflow: hidden; background: var(--white); }
  .poster {
    position: absolute; left: 298px; top: 0; width: 600px; height: 852px;
    background: radial-gradient(ellipse at 50% 45%, #ffffff 0%, var(--paper) 70%, #dcdce0 100%);
    border: 1px solid var(--blue);
    font-family: "Open Sans", sans-serif;
    overflow: hidden;
  }
  .title-bar {
    position: absolute; left: 0; top: 0; width: 100%; height: 38px;
    background: linear-gradient(#e8f5fe, var(--sky) 60%, var(--sky-deep));
    border-bottom: 2px solid var(--blue);
    display: flex; align-items: center; justify-content: center;
  }
  .title-bar h1 {
    font-family: "Righteous", sans-serif; font-weight: 400; font-size: 23px;
    color: var(--navy); letter-spacing: 0.5px;
  }
  .fund-badge {
    position: absolute; width: 156px; height: 156px; border-radius: 50%;
    background: radial-gradient(circle at 45% 30%, #9fd6ff 0%, #2f8fe0 45%, #0b3f9e 100%);
    border: 3px solid #d9e6f3;
    box-shadow: 0 5px 9px rgba(0,0,0,.35);
    display: flex; align-items: center; justify-content: center;
  }
  .fund-badge--big { left: 74px; top: 40px; }
  .fund-badge--small { left: 372px; top: 40px; }
  .fund-badge .word {
    font-family: "Passion One", sans-serif; font-weight: 700; color: #3fa33f;
    text-shadow: 0 0 2px #fff, 0 0 4px #fff;
  }
  .fund-badge--big .word { font-size: 74px; margin-top: -26px; }
  .fund-badge--small .word { font-size: 28px; letter-spacing: 2px; margin-top: -24px; }
  .badge-art {
    position: absolute; bottom: 30px; left: 50%; transform: translateX(-50%);
    background: linear-gradient(#c9e6c5, #6ea56a); border-radius: 2px;
  }
  .fund-badge--big .badge-art { width: 100px; height: 30px; }
  .fund-badge--small .badge-art { width: 40px; height: 22px; background: linear-gradient(#f2d68a, #b48a2e); }
  .or {
    position: absolute; left: 270px; top: 100px; width: 60px; text-align: center;
    font-family: "Righteous", sans-serif; font-size: 30px; color: var(--orange-text);
    -webkit-text-stroke: 1px #2a2a2a;
  }
  .column-label {
    position: absolute; top: 195px; width: 260px; text-align: center;
    font-family: "Righteous", sans-serif; font-size: 16px; color: var(--navy);
  }
  .column-label--big { left: 20px; }
  .column-label--small { left: 320px; }
  .perk { position: absolute; display: flex; align-items: center; gap: 14px; }
  .perk-icon {
    flex: none; width: 38px; height: 38px; border-radius: 3px;
    border: 2px solid var(--orange);
    background: linear-gradient(#4fb0f2, #0d5fb8);
    box-shadow: 1px 2px 3px rgba(0,0,0,.3);
  }
  .perk-label {
    font-family: "Passion One", sans-serif; font-size: 19px; line-height: 17px;
    color: var(--orange-text); text-transform: uppercase;
    text-shadow: 1px 1px 0 #5a4a2a, 2px 2px 2px rgba(0,0,0,.35);
  }
  .did-you-know {
    position: absolute; left: 337px; top: 433px; width: 222px; height: 203px;
    border: 1px solid var(--blue);
    background: linear-gradient(#ffffff 0%, #e6f3fd 35%, #6fbcf1 100%);
    padding: 8px 8px 0; color: var(--ink);
  }
  .did-you-know h2 {
    font-family: "Righteous", sans-serif; font-weight: 400; font-size: 25px;
    color: var(--navy); text-align: center; line-height: 28px;
  }
  .did-you-know .lead { font-size: 6px; font-weight: 700; text-align: center; line-height: 7.5px; margin-top: 4px; }
  .did-you-know .source { font-size: 5px; font-style: italic; text-align: center; }
  .did-you-know h3 {
    font-family: "Righteous", sans-serif; font-weight: 400; font-size: 11px;
    color: var(--navy); text-align: center; margin: 4px 0 6px;
  }
  .did-you-know ul { list-style: none; font-size: 9px; line-height: 13.2px; padding-left: 3px; }
  .did-you-know ul li::before { content: "• "; }
  .did-you-know .footnote { font-size: 6px; margin-top: 8px; padding-left: 3px; }
  .challenge {
    position: absolute; left: 0; top: 642px; width: 100%; height: 176px;
    background: var(--orange); padding-top: 6px;
  }
  .challenge .tagline {
    font-family: "Righteous", sans-serif; font-size: 10.5px; color: var(--navy);
    text-align: center; line-height: 25px;
  }
  .challenge h2 {
    font-family: "Righteous", sans-serif; font-weight: 400; font-size: 27px;
    color: var(--white); text-align: center; margin-top: 1px;
    text-shadow: 1px 1px 0 var(--navy), -1px -1px 0 var(--navy), 1px -1px 0 var(--navy), -1px 1px 0 var(--navy), 2px 3px 3px rgba(0,0,0,.4);
  }
  .challenge ul { list-style: none; padding-left: 9px; margin-top: 3px; font-size: 10.3px; line-height: 14.2px; color: var(--ink); }
  .challenge ul li::before { content: "• "; }
  .contact-bar {
    position: absolute; left: 0; top: 818px; width: 100%; height: 34px;
    background: linear-gradient(#e8f5fe, var(--sky) 55%, var(--sky-deep));
    border-top: 2px solid var(--blue);
    display: flex; align-items: center; padding-left: 10px; gap: 24px;
    font-family: "Righteous", sans-serif; font-size: 24px; color: var(--navy);
  }
</style>
</head>
<body>
<main class="poster">
  <header class="title-bar"><h1>There Are Only Two Types of Retirement Funds...</h1></header>

  <div class="fund-badge fund-badge--big">
    <span class="word">BIG</span>
    <span class="badge-art" role="img" aria-label="Stacks of banknotes"></span>
  </div>
  <div class="or">OR</div>
  <div class="fund-badge fund-badge--small">
    <span class="word">SMALL</span>
    <span class="badge-art" role="img" aria-label="A few coins"></span>
  </div>

  <div class="column-label column-label--big">Big Retirement Funds</div>
  <div class="column-label column-label--small">Small Retirement Funds</div>

  <div class="perk" style="left:56px;top:219px"><span class="perk-icon" role="img" aria-label="Eiffel tower icon"></span><span class="perk-label">Foreign Travel</span></div>
  <div class="perk" style="left:56px;top:266px"><span class="perk-icon" role="img" aria-label="Sailboat icon"></span><span class="perk-label">Sailing</span></div>
  <div class="perk" style="left:56px;top:313px"><span class="perk-icon" role="img" aria-label="Concert tickets icon"></span><span class="perk-label">Concerts</span></div>
  <div class="perk" style="left:56px;top:362px"><span class="perk-icon" role="img" aria-label="Parachute icon"></span><span class="perk-label">Sky Diving</span></div>
  <div class="perk" style="left:56px;top:411px"><span class="perk-icon" role="img" aria-label="Fishing rod icon"></span><span class="perk-label">Fishing</span></div>
  <div class="perk" style="left:56px;top:460px"><span class="perk-icon" role="img" aria-label="Golfer icon"></span><span class="perk-label">Golf</span></div>
  <div class="perk" style="left:56px;top:506px"><span class="perk-icon" role="img" aria-label="Wine glasses icon"></span><span class="perk-label">Fine Dining</span></div>
  <div class="perk" style="left:56px;top:551px"><span class="perk-icon" role="img" aria-label="Palm tree icon"></span><span class="perk-label">Sandy Beaches</span></div>
  <div class="perk" style="left:56px;top:600px"><span class="perk-icon" role="img" aria-label="Toys icon"></span><span class="perk-label">Spoiling<br>Grandchildren</span></div>

  <div class="perk" style="left:334px;top:224px"><span class="perk-icon" role="img" aria-label="Coins icon"></span><span class="perk-label">Counting<br>Every Penny</span></div>
  <div class="perk" style="left:334px;top:270px"><span class="perk-icon" role="img" aria-label="Armchair icon"></span><span class="perk-label">Sitting At<br>Home</span></div>
  <div class="perk" style="left:334px;top:318px"><span class="perk-icon" role="img" aria-label="Thermometer icon"></span><span class="perk-label">Turning Off The<br>Heat In Winter</span></div>
  <div class="perk" style="left:334px;top:368px"><span class="perk-icon" role="img" aria-label="Open hand icon"></span><span class="perk-label">Relying On<br>Family, Friends<br>And Charity</span></div>

  <aside class="did-you-know">
    <h2>Did You Know?</h2>
    <p class="lead">1 in 5 people retiring in 2013 will be below the poverty line?<br>In the UK, 14% will rely solely on a state pension.<br>That's less than AED 640 per week.</p>
    <p class="source">(Source: Harrowgate Cohort of 2013)</p>
    <h3>Of 100 people aged 25 today, by age 65</h3>
    <ul>
      <li>1 will be wealthy</li>
      <li>4 will be financially independent</li>
      <li>5 will still be working</li>
      <li>12 will be bankrupt</li>
      <li>29 will already be dead</li>
      <li>49 will be dependent on others</li>
    </ul>
    <p class="footnote">Of those still living, 86% will rely on friends, relatives and charity.</p>
  </aside>

  <section class="challenge">
    <p class="tagline">Big pensions are acquired over the length of a career with careful planning and motivation</p>
    <p class="tagline">Small pensions take no effort at all</p>
    <h2>Which Are You Aiming For?</h2>
    <ul>
      <li>To retire on $30,000 per annum, you'll need approx.. $600,000 in today's terms.</li>
      <li>That's $1,456,380 in 30 years with 3% inflation.</li>
      <li>By saving in a bank earning ZERO interest, you need to save $4,045 each month for 30 years</li>
      <li>If you invest in the markets and earn 5% interest each year, you only need to save $2,307 each month.</li>
      <li>If you manage to get 10% per annum interest, you'll only need to save $934 per month. That's less than AED 3,450.</li>
    </ul>
  </section>

  <footer class="contact-bar">
    <span>E: rmoss@tidalnest.com</span>
    <span>M: 050 8126 473</span>
  </footer>
</main>
</body>
</html>
```